Bold Cover needed for a book on Workplace Bullying

I need a book cover design for a book titled, “Iron Silence?” The book recounts my story of bullying in the workplace. It also includes chapters on how readers can minimize/stop workplace bullying, write an effective complaint, and ensure their own mental wellbeing.
I am looking for a bold design using red and black, and possibly distressed lettering. The covers of other books dealing with this subject do not reflect my vision. They are often too childish or look too academic. This book needs to stress the serious nature of a toxic workplace, while appealing to readers experiencing a similar situation. I’d like the cover to reflect the mental anguish associated with workplace bullying (hence the distressed lettering).
I have included a cover that appeals to me (although the coloring is wrong). That said, I am also very happy (and excited) to see your creative input!
On the cover, it should have the following:
Title: Iron Silence?
Subtitle: How the Harbour Works Department Condones Bullying & Ruins Lives
Author: Owen Frick
Other relevant details:
Book size: 5.5” x 8.5”
Back cover will have a blurb, author picture/short bio, and barcode
The blurb on the back cover reads:
Undermining, intimidation and threats
Despite the Department of Harbour Works allegedly holding a zero tolerance for bullying, these behaviours were an everyday occurrence in at least one workplace. Even after a decade of complaints, numerous witnesses and physical proof, the department failed to act. Instead, they looked the other way, allowing one powerful and well-connected individual to end careers and ruin lives.
After being targeted, one teacher resolved to put an end to the abuse experienced by more than fifty employees. His startling story reveals the relentless bullying, mental health ramifications, and insidious tactics used to cover up the corrosive behaviour.
Those who have experienced a toxic workplace will also find much needed support and guidance, intended to minimise suffering and detail a clear way forward. Chapters include dealing with bullying in the workplace, how to lodge a successful complaint, and how to stay sane during any potential legal action.

```html
<!DOCTYPE html>
<html lang="en">
<head>
<meta charset="utf-8">
<title>Iron Silence? — Owen Frick</title>
<link rel="stylesheet" href="https://fonts.googleapis.com/css2?family=Cinzel:wght@700;900&family=Montserrat:wght@400&display=swap">
<style>
  :root {
    --page: #ffffff;
    --cover: #333333;
    --red: #dc4034;
    --ink-light: #f2f2f2;
    --print-tone: #8a8a8a;
  }
  html, body {
    margin: 0;
    padding: 0;
    width: 1200px;
    height: 1077px;
    overflow: hidden;
    background: var(--page);
  }
  .canvas {
    position: relative;
    width: 1200px;
    height: 1077px;
  }
  .filters { position: absolute; width: 0; height: 0; }
  .cover {
    position: absolute;
    left: 273px;
    top: 51px;
    width: 642px;
    height: 965px;
    background: var(--cover);
    overflow: hidden;
  }
  .title-main,
  .title-sub,
  .author {
    position: absolute;
    left: 0;
    width: 100%;
    margin: 0;
    text-align: center;
    font-family: "Cinzel", "Times New Roman", serif;
    font-weight: 900;
    line-height: 1;
    filter: url(#distress);
  }
  .title-main {
    top: 60px;
    font-size: 190px;
    color: var(--red);
    letter-spacing: -2px;
  }
  .title-sub {
    top: 232px;
    font-size: 78px;
    color: var(--red);
    letter-spacing: -1px;
  }
  .emblem {
    position: absolute;
    left: 137px;
    top: 361px;
    width: 368px;
    height: 368px;
  }
  .subtitle {
    position: absolute;
    top: 757px;
    left: 0;
    width: 100%;
    margin: 0;
    text-align: center;
    font-family: "Montserrat", Arial, sans-serif;
    font-weight: 400;
    font-size: 24px;
    line-height: 26px;
    letter-spacing: 0.6px;
    color: var(--ink-light);
  }
  .author {
    top: 862px;
    font-size: 66px;
    font-weight: 700;
    color: var(--ink-light);
    letter-spacing: 1px;
    word-spacing: 12px;
  }
</style>
</head>
<body>
<div class="canvas">
  <svg class="filters" aria-hidden="true">
    <filter id="distress" x="0" y="0" width="100%" height="100%">
      <feTurbulence type="fractalNoise" baseFrequency="0.9" numOctaves="2" seed="4" result="noise"/>
      <feColorMatrix in="noise" type="matrix" values="0 0 0 0 0  0 0 0 0 0  0 0 0 0 0  0 0 0 -2.4 1.5" result="holes"/>
      <feComposite in="SourceGraphic" in2="holes" operator="in"/>
    </filter>
  </svg>

  <section class="cover">
    <h1 class="title-main">IRON</h1>
    <p class="title-sub">SILENCE?</p>

    <svg class="emblem" viewBox="0 0 368 368">
      <defs>
        <radialGradient id="print-fill" cx="50%" cy="52%" r="50%">
          <stop offset="0%" stop-color="var(--print-tone)" stop-opacity="0.55"/>
          <stop offset="100%" stop-color="var(--cover)" stop-opacity="0"/>
        </radialGradient>
      </defs>
      <circle cx="184" cy="184" r="158" fill="url(#print-fill)" role="img"
              aria-label="White distressed handprint, palm raised in a stop gesture"/>
      <circle cx="184" cy="184" r="170" fill="none" stroke="var(--red)" stroke-width="12" filter="url(#distress)"/>
    </svg>

    <p class="subtitle">How the Harbour Works Department<br>Condones Bullying &amp; Ruins Lives</p>

    <p class="author">OWEN FRICK</p>
  </section>
</div>
</body>
</html>
```